brix4lane

i want to ues this logo and the same colors used on the business card

cleaning & service

Industry/Entity Type

Business

Contact Information for Business Card

Font styles to use
Serif
Sans Serif
Decorative
Script

Colors
add136
0692cd
000000
5c5c5c
fbfbfb

Requirements
Must have
• cleaning things

```html
<!DOCTYPE html>
<html lang="en">
<head>
<meta charset="utf-8">
<title>brix4lane business card</title>
<link rel="stylesheet" href="https://fonts.googleapis.com/css2?family=Questrial&family=Kaushan+Script&display=swap">
<style>
  :root {
    --green: #add136;
    --blue: #0692cd;
    --black: #000000;
    --grey: #5c5c5c;
    --paper: #fbfbfb;
    --stage: #e9e6e0;
  }
  * { box-sizing: border-box; margin: 0; padding: 0; }
  html, body { width: 1200px; height: 780px; overflow: hidden; }
  body {
    background: var(--stage);
    display: flex;
    align-items: center;
    justify-content: center;
    gap: 80px;
    font-family: "Questrial", sans-serif;
  }
  .card {
    position: relative;
    width: 380px;
    height: 600px;
    background: var(--paper);
    border-radius: 22px;
    box-shadow: 0 6px 18px rgba(0,0,0,0.12);
    overflow: hidden;
  }
  .card--back {
    display: flex;
    flex-direction: column;
    align-items: center;
    padding-top: 120px;
  }
  .brand-mark {
    display: flex;
    align-items: center;
    gap: 12px;
  }
  .brand-dot {
    width: 16px;
    height: 16px;
    border-radius: 50%;
    background: var(--green);
  }
  .brand-name {
    font-family: "Questrial", sans-serif;
    color: var(--blue);
    font-size: 44px;
    letter-spacing: 1px;
  }
  .person-name {
    font-family: "Kaushan Script", cursive;
    color: var(--blue);
    font-size: 34px;
    margin-top: 70px;
  }
  .divider {
    width: 280px;
    height: 2px;
    background: var(--green);
    margin: 22px 0 26px;
  }
  .contact {
    display: flex;
    flex-direction: column;
    align-items: center;
    gap: 8px;
    margin-bottom: 22px;
  }
  .contact-icon { width: 30px; height: 30px; }
  .contact-text { color: var(--blue); font-size: 21px; letter-spacing: 0.5px; }
  .card--front .brand-mark {
    position: absolute;
    top: 70px;
    left: 0;
    right: 0;
    justify-content: center;
  }
  .front-band {
    position: absolute;
    left: 0;
    bottom: 0;
    width: 100%;
    height: 300px;
  }
  .cleaning-illustration {
    position: absolute;
    top: 175px;
    left: 45px;
    width: 300px;
    height: 345px;
    border-radius: 6px;
    background: linear-gradient(160deg, var(--blue) 0%, #3fa9d6 50%, var(--green) 100%);
    z-index: 1;
  }
</style>
</head>
<body>
  <section class="card card--back" aria-label="Business card back">
    <div class="brand-mark">
      <span class="brand-dot"></span>
      <span class="brand-name">brix4lane</span>
    </div>
    <p class="person-name">Maya Ortiz</p>
    <div class="divider"></div>
    <div class="contact">
      <svg class="contact-icon" viewBox="0 0 30 30" aria-hidden="true">
        <circle cx="15" cy="15" r="14" fill="none" stroke="var(--green)" stroke-width="2"/>
        <rect x="10.5" y="8" width="9" height="14" rx="1.5" fill="none" stroke="var(--green)" stroke-width="2"/>
        <circle cx="15" cy="19" r="1" fill="var(--green)"/>
      </svg>
      <span class="contact-text">+1 (555) 014 2238</span>
    </div>
    <div class="contact">
      <svg class="contact-icon" viewBox="0 0 30 30" aria-hidden="true">
        <circle cx="15" cy="15" r="14" fill="var(--green)"/>
        <rect x="8" y="10" width="14" height="10" fill="none" stroke="var(--paper)" stroke-width="1.8"/>
        <path d="M8 10 L15 16 L22 10" fill="none" stroke="var(--paper)" stroke-width="1.8"/>
      </svg>
      <span class="contact-text">hello@brix4lane.com</span>
    </div>
  </section>

  <section class="card card--front" aria-label="Business card front">
    <div class="brand-mark">
      <span class="brand-dot"></span>
      <span class="brand-name">brix4lane</span>
    </div>
    <svg class="front-band" viewBox="0 0 380 300" preserveAspectRatio="none" aria-hidden="true">
      <path d="M0 300 L0 250 Q190 230 380 90 L380 300 Z" fill="var(--green)"/>
      <path d="M0 240 Q190 215 380 70" fill="none" stroke="var(--blue)" stroke-width="3" opacity="0.5"/>
    </svg>
    <div class="cleaning-illustration" role="img" aria-label="Large illustration of blue city buildings with a green broom and sparkles, representing cleaning services"></div>
  </section>
</body>
</html>
```